Harborline Works Buisness Cards

Provide a business card layout

Peter Landry
PO Box 915
Kestrel Cove MA 02190
peter@hworksllc-example.com

Industry/Entity Type

Business

Font styles to use
Serif

Colors
f04a50

```html
<!DOCTYPE html>
<html lang="en">
<head>
<meta charset="utf-8">
<title>Harborline Works Business Cards</title>
<link rel="stylesheet" href="https://fonts.googleapis.com/css2?family=Tinos:wght@400;700&display=swap">
<style>
  :root {
    --brand-red: #990000;
    --brand-orange: #e89a2c;
    --ink: #1e1e1e;
    --muted: #8a8a8a;
    --card-white: #ffffff;
    --stage-light: #d9d9d9;
    --stage-dark: #5e5e5e;
    --rule: #c9c9c9;
  }
  * { box-sizing: border-box; margin: 0; padding: 0; }
  html, body { width: 1200px; height: 822px; overflow: hidden; }
  body {
    font-family: "Tinos", "Times New Roman", serif;
    background: radial-gradient(ellipse at 50% 60%, var(--stage-light) 0%, #a9a9a9 45%, var(--stage-dark) 100%);
    position: relative;
  }
  .card {
    position: absolute;
    width: 557px;
    height: 307px;
    border-radius: 18px;
    background: var(--card-white);
    box-shadow: 4px 6px 12px rgba(0,0,0,0.35);
    overflow: hidden;
  }
  .card--split { left: 27px; top: 86px; overflow: visible; }
  .card--swoosh { left: 608px; top: 86px; }
  .card--divided { left: 306px; top: 430px; }

  .brand {
    position: absolute;
    display: flex;
    flex-direction: column;
    align-items: center;
    gap: 8px;
    transform: translate(-50%, -50%);
  }
  .brand__dot {
    width: 34px; height: 34px;
    border-radius: 50%;
    background: var(--brand-orange);
  }
  .brand__name {
    font-size: 21px;
    font-weight: 700;
    color: var(--ink);
    letter-spacing: 0.5px;
    white-space: nowrap;
  }

  .person {
    position: absolute;
    font-size: 28px;
    line-height: 1;
    white-space: nowrap;
  }
  .person__first { color: var(--brand-red); }
  .person__last { color: var(--ink); }
  .contact {
    position: absolute;
    list-style: none;
    font-size: 14px;
    line-height: 26px;
    color: var(--muted);
    white-space: nowrap;
  }

  /* split card */
  .split__panel {
    position: absolute;
    left: 279px; top: 0;
    width: 278px; height: 307px;
    background: var(--brand-red);
    border-radius: 18px;
  }
  .split__notch {
    position: absolute;
    left: -12px; top: 144px;
    width: 0; height: 0;
    border-top: 12px solid transparent;
    border-bottom: 12px solid transparent;
    border-right: 12px solid var(--brand-red);
  }
  .card--split .person { left: 328px; top: 96px; }
  .card--split .person__first { color: var(--brand-orange); }
  .card--split .person__last { color: #111; }
  .card--split .contact { left: 328px; top: 141px; color: #ffffff; }

  /* swoosh card */
  .swoosh { position: absolute; inset: 0; }
  .card--swoosh .person { left: 40px; top: 92px; }
  .card--swoosh .contact { left: 40px; top: 141px; }

  /* divided card */
  .divider {
    position: absolute;
    left: 288px; top: 66px;
    width: 1px; height: 168px;
    background: var(--rule);
  }
  .card--divided .person { left: 332px; top: 92px; }
  .card--divided .contact { left: 332px; top: 143px; }
</style>
</head>
<body>

  <section class="card card--split">
    <div class="brand" style="left:146px; top:154px;">
      <span class="brand__dot"></span>
      <span class="brand__name">Harborline Works</span>
    </div>
    <div class="split__panel"><span class="split__notch"></span></div>
    <p class="person"><span class="person__first">Peter</span> <span class="person__last">Landry</span></p>
    <ul class="contact">
      <li>PO Box 915</li>
      <li>Kestrel Cove MA 02190</li>
      <li>peter@hworksllc-example.com</li>
    </ul>
  </section>

  <section class="card card--swoosh">
    <svg class="swoosh" width="557" height="307" viewBox="0 0 557 307" aria-hidden="true">
      <path d="M0,244 C160,312 430,318 557,70 L557,307 L0,307 Z" fill="#bdbdbd"/>
      <path d="M0,250 C165,318 436,322 557,80 L557,307 L0,307 Z" fill="var(--brand-red)"/>
    </svg>
    <div class="brand" style="left:420px; top:74px;">
      <span class="brand__dot"></span>
      <span class="brand__name">Harborline Works</span>
    </div>
    <p class="person"><span class="person__first">Peter</span> <span class="person__last">Landry</span></p>
    <ul class="contact">
      <li>PO Box 915</li>
      <li>Kestrel Cove MA 02190</li>
      <li>peter@hworksllc-example.com</li>
    </ul>
  </section>

  <section class="card card--divided">
    <div class="brand" style="left:148px; top:148px;">
      <span class="brand__dot"></span>
      <span class="brand__name">Harborline Works</span>
    </div>
    <span class="divider"></span>
    <p class="person"><span class="person__first">Peter</span> <span class="person__last">Landry</span></p>
    <ul class="contact">
      <li>PO Box 915</li>
      <li>Kestrel Cove MA 02190</li>
      <li>peter@hworksllc-example.com</li>
    </ul>
  </section>

</body>
</html>
```